International wholesale business needs a business card

We need a business card.

Company Details:
Company Name and logo
Address, Phone number, Website
Employee Details:
Name, Designation, Mobile Number & Email address

```html
<!DOCTYPE html>
<html lang="en">
<head>
<meta charset="UTF-8">
<title>Veranto Trading – Business Card</title>
<link href="https://fonts.googleapis.com/css2?family=Playfair+Display:wght@700&family=Poppins:wght@400;500&display=swap" rel="stylesheet">
<style>
  :root {
    --stage: #2b2b2c;
    --card-white: #ffffff;
    --card-black: #1c1d1f;
    --card-black-light: #34363a;
    --brand-red: #c8202a;
    --ink: #1a1a1a;
    --ink-soft: #333333;
    --rule: #9a9a9a;
  }
  * { box-sizing: border-box; margin: 0; padding: 0; }
  html, body {
    width: 1200px; height: 1108px; overflow: hidden;
    background: var(--stage);
  }
  .canvas { position: relative; width: 1200px; height: 1108px; }
  .card {
    position: absolute; top: 214px; width: 420px; height: 680px;
    border-radius: 24px; overflow: hidden;
  }
  .card-front {
    left: 150px; background: var(--card-white);
    display: flex; flex-direction: column; align-items: center;
    font-family: 'Poppins', sans-serif; color: var(--ink);
    text-align: center;
  }
  .card-back { left: 630px; background: var(--card-black); }

  .brand-name {
    margin-top: 128px;
    font-family: 'Playfair Display', serif; font-weight: 700;
    color: var(--brand-red); font-size: 34px; line-height: 1.1;
    letter-spacing: 2px; text-align: center;
  }
  .person-name {
    margin-top: 118px;
    font-family: 'Playfair Display', serif; font-weight: 700;
    color: var(--brand-red); font-size: 32px; letter-spacing: 1px;
  }
  .person-role { font-size: 19px; color: var(--ink-soft); margin-top: 2px; }
  .icon-row { margin-top: 16px; display: flex; align-items: center; gap: 8px; }
  .icon-row .rule { width: 46px; height: 1px; background: var(--rule); }
  .icon-tile {
    width: 34px; height: 34px; border-radius: 6px; background: var(--brand-red);
    display: flex; align-items: center; justify-content: center;
  }
  .icon-tile svg { width: 20px; height: 20px; }
  .contact-list { margin-top: 12px; font-size: 18.5px; line-height: 1.36; }
  .contact-list .accent { color: var(--brand-red); }
  .divider { width: 290px; height: 1px; background: var(--rule); margin: 8px 0; }
  .address { font-size: 18.5px; line-height: 1.36; }

  .back-pattern {
    position: absolute; inset: 0;
    background: radial-gradient(circle at 85% 15%, var(--card-black-light) 0%, var(--card-black) 65%);
  }
  .back-brand {
    position: absolute; left: 0; right: 0; top: 440px;
    text-align: center;
    font-family: 'Playfair Display', serif; font-weight: 700;
    color: var(--brand-red); font-size: 20px; letter-spacing: 2px;
  }
</style>
</head>
<body>
<main class="canvas">
  <section class="card card-front">
    <div class="brand-name">VERANTO<br>TRADING</div>

    <h1 class="person-name">DANIEL MARSH</h1>
    <p class="person-role">Managing Director</p>

    <div class="icon-row">
      <span class="rule"></span>
      <span class="icon-tile" aria-label="Phone">
        <svg viewBox="0 0 24 24" fill="none" stroke="#fff" stroke-width="2"><path d="M5 4h4l2 5-2.5 1.5a11 11 0 0 0 5 5L15 13l5 2v4a2 2 0 0 1-2 2A16 16 0 0 1 3 6a2 2 0 0 1 2-2z"/></svg>
      </span>
      <span class="icon-tile" aria-label="Mobile">
        <svg viewBox="0 0 24 24" fill="none" stroke="#fff" stroke-width="2"><rect x="7" y="2" width="10" height="20" rx="2"/><line x1="11" y1="18" x2="13" y2="18"/></svg>
      </span>
      <span class="icon-tile" aria-label="Email">
        <svg viewBox="0 0 24 24" fill="none" stroke="#fff" stroke-width="2"><rect x="3" y="5" width="18" height="14" rx="1"/><path d="M3 6l9 7 9-7"/></svg>
      </span>
      <span class="icon-tile" aria-label="Website">
        <svg viewBox="0 0 24 24" fill="none" stroke="#fff" stroke-width="2"><circle cx="12" cy="12" r="9"/><path d="M3 12h18M12 3a14 14 0 0 1 0 18M12 3a14 14 0 0 0 0 18"/></svg>
      </span>
      <span class="rule"></span>
    </div>

    <div class="contact-list">
      <p>044-123 456 789</p>
      <p>044-123 456 789</p>
      <p>info@verantotrade.com</p>
      <p>www.<span class="accent">verantotrade</span>.com</p>
    </div>
    <div class="divider"></div>
    <div class="address">
      <p>421, Address line goes here</p>
      <p>45452,Country Name</p>
    </div>
  </section>

  <section class="card card-back">
    <div class="back-pattern" role="img" aria-label="Embossed repeating brand pattern on the black card back"></div>
    <div class="back-brand">VERANTO TRADING</div>
  </section>
</main>
</body>
</html>
```